Astrology Web Site in Need of a Clean & Modern Design

Over the past few months we've converted our site to Wordpress. With the content and structure now in place, it's time for a clean, modern design. Our new site must engage visitors, delivering insights and guidance through a well designed UI/UX. We're taking online astrology to the next level! We've sourced hundreds of amazing images and with the eye of a talented designer we can achieve our goals. Our Wordpress developer is ready to convert your design and launch a truly showcase site. Attached are a few examples of what we would like the design to be modeled on. Further details are included in the attached document "Templates to Design for StarlitPathway.net"

Target Market(s)

female

Industry/Entity Type

Online

Number of Pages Required

4 page

Requirements
Must have
• Use real images and not illustrations.
• Use a 12-columns grid system.
• Zodiac signs/icons should be of a single color with no gradients.
Should not have
• crystals balls, fortune tellers etc...dark and heavy backgrounds (ignore current site design and color).

```html
<!DOCTYPE html>
<html lang="en">
<head>
<meta charset="utf-8">
<title>Leo Daily Horoscope – StarlitPathway.net</title>
<link href="https://fonts.googleapis.com/css2?family=Open+Sans:wght@400;600;700&family=Noticia+Text:ital,wght@0,400;0,700;1,400&display=swap" rel="stylesheet">
<style>
:root{
  --pink:#c8305a;
  --blue:#2a78b4;
  --ink:#2b2b2b;
  --muted:#777;
  --text:#555;
  --light:#efefef;
  --line:#dcdcdc;
  --white:#fff;
  --footer:#1e1e1e;
}
*{box-sizing:border-box;margin:0;padding:0}
html,body{width:1200px;height:5373px;overflow:hidden}
body{font-family:"Open Sans",Arial,sans-serif;color:var(--ink);background:var(--white)}
.wrap{width:1040px;margin:0 auto;position:relative;height:100%}
section,header,footer{position:relative;width:1200px}
.glyphs{font-family:"Segoe UI Symbol","Noto Sans Symbols",sans-serif}

/* photo areas: layered soft tones, shared vignette */
.ph{position:relative;overflow:hidden}
.ph::after{content:"";position:absolute;inset:0;box-shadow:inset 0 0 60px rgba(0,0,0,.35);pointer-events:none}
.ph>*{position:relative;z-index:1}

/* hero */
.hero{height:627px;background:
  radial-gradient(ellipse 18% 30% at 66% 34%,rgba(250,225,175,.95),transparent 70%),
  radial-gradient(ellipse 30% 55% at 68% 58%,rgba(205,145,70,.9),transparent 72%),
  radial-gradient(ellipse 40% 40% at 22% 30%,rgba(225,190,130,.55),transparent 75%),
  radial-gradient(ellipse 35% 50% at 92% 40%,rgba(120,80,35,.7),transparent 75%),
  linear-gradient(180deg,#6a4a22 0%,#a07a42 35%,#b88e56 62%,#8a6530 85%,#5a3e1c 100%)}
.hero::after{content:"";position:absolute;inset:0;background:linear-gradient(180deg,rgba(0,0,0,.2),transparent 20%,transparent 70%,rgba(0,0,0,.35))}
.hero .wrap{z-index:1}
.brand{position:absolute;left:10px;top:26px;color:var(--white);font-weight:700;font-size:22px;line-height:1}
.brand small{display:block;font-weight:700;font-size:13px;margin-top:7px}
.main-nav{position:absolute;right:0;top:30px;display:flex;gap:22px;font-size:13px;color:var(--white)}
.main-nav a{color:inherit;text-decoration:none;padding:5px 10px}
.main-nav a.active{border:1px solid var(--white)}
.sign-title{position:absolute;left:44px;top:242px;color:var(--white);font-family:"Noticia Text",Georgia,serif;font-size:80px;line-height:1}
.sign-sub{position:absolute;left:38px;top:350px;color:var(--white);font-family:"Noticia Text",Georgia,serif;font-style:italic;font-size:26px}
.sign-dates{position:absolute;left:64px;top:390px;color:var(--white);font-size:11px}
.zodiac{position:absolute;left:0;top:505px;width:1040px;display:flex;justify-content:space-between}
.zodiac li{list-style:none;width:70px;text-align:center;color:var(--white);font-size:12px}
.zodiac .glyph{display:flex;align-items:center;justify-content:center;width:66px;height:66px;margin:0 auto 8px;border:2px solid var(--white);font-size:38px}
.zodiac li.on .glyph{background:rgba(255,255,255,.2)}

/* daily */
.daily{height:473px}
.daily h1{position:absolute;left:0;top:54px;font-size:30px;font-weight:700;display:flex;align-items:center;gap:12px}
.leo-mark{color:var(--pink);font-size:34px}
.daily .date{position:absolute;left:48px;top:104px;font-size:12px;color:var(--muted)}
.tabs{position:absolute;left:0;top:140px;width:690px;display:flex;border-bottom:1px solid var(--line)}
.tabs span{padding:10px 26px;font-size:14px;color:var(--blue)}
.tabs span.active{color:var(--ink);border:1px solid var(--line);border-bottom-color:var(--white);margin-bottom:-1px;background:var(--white)}
.daily .text{position:absolute;left:0;top:200px;width:690px;font-size:13px;line-height:21px;color:var(--text)}
.meta{position:absolute;left:0;top:300px;font-size:12px;color:var(--text)}
.meta b{font-weight:700;color:var(--ink);margin-right:6px}
.meta span{margin-right:26px}
.btn{display:inline-block;background:var(--pink);color:var(--white);font-size:13px;font-weight:600;padding:10px 22px;border-radius:3px}
.daily .btn{position:absolute;left:0;top:348px}
.daily .photo{position:absolute;left:715px;top:95px;width:325px;height:250px;background:
  radial-gradient(ellipse 28% 36% at 52% 42%,rgba(240,200,130,.95),transparent 72%),
  radial-gradient(ellipse 45% 40% at 50% 78%,rgba(170,115,55,.9),transparent 75%),
  radial-gradient(ellipse 50% 60% at 15% 30%,rgba(110,80,40,.8),transparent 70%),
  linear-gradient(170deg,#8a6a3a,#b8894c 50%,#6e4c22)}
.rating{position:absolute;left:715px;top:372px;font-size:12px;font-weight:700;display:flex;align-items:center;gap:8px}
.rating i{width:13px;height:13px;border-radius:50%;background:#888;display:inline-block}
.rating i.off{background:none;border:1.5px solid #aaa}

/* horoscope cards */
.periods{height:412px;background:var(--light)}
.cards{position:absolute;top:48px;left:0;width:1040px;display:flex;justify-content:space-between}
.card{width:325px}
.card .photo{height:218px;display:flex;align-items:center;justify-content:center;color:var(--white);font-family:"Noticia Text",Georgia,serif;font-weight:700;font-size:32px;line-height:1.05;text-align:center;text-shadow:0 2px 6px rgba(0,0,0,.45)}
.card.sel .photo{outline:4px solid var(--pink);outline-offset:-4px}
.card p{margin-top:18px;font-size:12px;line-height:18px;color:var(--text)}
.more{display:inline-block;margin-top:14px;font-size:12px;font-weight:700;color:var(--blue)}

/* compatibility */
.compat{height:695px}
.sec-title{position:absolute;left:0;width:1040px;text-align:center;font-size:28px;font-weight:600}
.compat .sec-title{top:50px}
.overview{position:absolute;left:0;top:108px;width:1040px;height:243px;display:flex;align-items:center;padding-left:210px;background:
  radial-gradient(ellipse 14% 34% at 76% 58%,rgba(230,40,50,.95),transparent 72%),
  radial-gradient(ellipse 12% 30% at 86% 52%,rgba(215,30,40,.95),transparent 72%),
  radial-gradient(ellipse 40% 60% at 30% 40%,rgba(215,180,150,.7),transparent 72%),
  linear-gradient(180deg,#a07c60 0%,#c09a7a 45%,#8a5a40 75%,#5a3424 100%)}
.overlay-label{color:var(--white);font-family:"Noticia Text",Georgia,serif;font-weight:700;font-size:32px;text-shadow:0 2px 6px rgba(0,0,0,.5)}
.topics{position:absolute;left:0;top:390px;width:1040px;display:flex;justify-content:space-between}
.topic{width:233px;height:243px;display:flex;align-items:center;justify-content:center}
.t-dating{background:radial-gradient(ellipse 40% 45% at 40% 40%,rgba(220,190,170,.85),transparent 70%),radial-gradient(ellipse 40% 50% at 75% 70%,rgba(40,35,40,.9),transparent 70%),linear-gradient(160deg,#b8a090,#5a4640 60%,#2a2226)}
.t-marriage{background:radial-gradient(ellipse 30% 45% at 35% 55%,rgba(245,240,235,.95),transparent 70%),radial-gradient(ellipse 30% 50% at 72% 55%,rgba(40,40,45,.85),transparent 70%),linear-gradient(160deg,#b8c49a,#7a8a5a 55%,#4a5632)}
.t-passion{background:radial-gradient(ellipse 45% 25% at 50% 55%,rgba(200,30,30,.8),transparent 72%),radial-gradient(ellipse 30% 20% at 65% 72%,rgba(160,20,20,.7),transparent 70%),linear-gradient(160deg,#2a1414,#0c0606)}
.t-financial{background:radial-gradient(ellipse 35% 40% at 35% 40%,rgba(240,200,130,.9),transparent 70%),radial-gradient(ellipse 40% 40% at 75% 70%,rgba(150,95,40,.9),transparent 72%),linear-gradient(160deg,#c8965a,#8a5c2a 60%,#4a2e12)}

/* app banner */
.app{height:275px;background:
  radial-gradient(1px 1px at 12% 20%,#fff,transparent),radial-gradient(1px 1px at 28% 70%,#fff,transparent),
  radial-gradient(1px 1px at 44% 35%,#fff,transparent),radial-gradient(1.5px 1.5px at 55% 80%,#fff,transparent),
  radial-gradient(1px 1px at 62% 18%,#fff,transparent),radial-gradient(1px 1px at 85% 60%,#fff,transparent),
  radial-gradient(1.5px 1.5px at 93% 25%,#fff,transparent),radial-gradient(1px 1px at 36% 12%,#fff,transparent),
  radial-gradient(ellipse 40% 70% at 70% 50%,rgba(90,70,110,.45),transparent 75%),
  linear-gradient(90deg,#2c2c36,#1a1a24 55%,#2e2632)}
.app h2{position:absolute;left:0;top:78px;color:var(--white);font-weight:400;font-size:30px;line-height:40px}
.app h2 b{font-weight:700}
.app .btn{position:absolute;left:0;top:170px;padding:8px 18px;font-size:12px}
.phones{position:absolute;left:745px;top:35px;display:flex;gap:14px}
.phone{width:92px;height:190px;border-radius:14px;background:#111;border:3px solid #666;padding:22px 6px}
.phone div{width:100%;height:100%;background:radial-gradient(ellipse 45% 35% at 50% 45%,#e2c8b0,transparent 70%),linear-gradient(#6a5a50,#c8b4a0 60%,#4a3a34)}

/* pink bar */
.bar{height:90px;background:var(--pink);color:var(--white);display:flex;align-items:center;justify-content:center;gap:14px;font-size:28px;font-weight:600}
.bar .leo-mark{color:var(--white)}
.bar::before{content:"";position:absolute;left:50%;top:-16px;margin-left:-16px;border:16px solid transparent;border-top:0;border-bottom:16px solid var(--pink)}

/* carousels */
.row-sec .sec-title{top:50px}
.row-sec.grey{background:var(--light)}
.tiles{position:absolute;left:0;top:104px;width:1040px;display:flex;justify-content:space-between}
.tile{width:233px;text-align:center}
.tile .photo{height:233px}
.tile.sel .photo{outline:4px solid var(--pink);outline-offset:-4px}
.tile p{margin-top:24px;font-size:12px;line-height:18px;color:var(--text);padding:0 14px}
.arrow{position:absolute;top:206px;width:18px;height:30px}
.arrow.l{left:-62px}.arrow.r{right:-62px}

/* tile tones */
.p-lion{background:radial-gradient(ellipse 35% 40% at 55% 40%,rgba(235,180,100,.95),transparent 70%),radial-gradient(ellipse 50% 40% at 50% 85%,rgba(90,110,60,.8),transparent 72%),linear-gradient(170deg,#7a9ab8,#b8874a 45%,#5a4a28)}
.p-fire{background:radial-gradient(ellipse 45% 35% at 50% 70%,rgba(255,200,60,.95),transparent 70%),radial-gradient(ellipse 60% 45% at 50% 60%,rgba(230,80,20,.9),transparent 75%),linear-gradient(0deg,#c03a10,#2a0c04 70%,#0a0402)}
.p-sky{background:radial-gradient(ellipse 60% 35% at 40% 85%,rgba(240,240,240,.9),transparent 70%),radial-gradient(ellipse 40% 30% at 75% 20%,rgba(150,175,200,.7),transparent 70%),linear-gradient(180deg,#34506e,#6c88a6 55%,#b8c6d2)}
.p-planet{background:radial-gradient(circle at 38% 38%,rgba(255,240,170,1) 0,rgba(240,190,70,.9) 10%,transparent 30%),radial-gradient(ellipse 60% 50% at 70% 75%,rgba(70,110,60,.9),transparent 70%),linear-gradient(160deg,#1a2010,#0a0c08)}
.p-couple{background:radial-gradient(ellipse 40% 45% at 45% 65%,rgba(30,30,34,.9),transparent 70%),radial-gradient(ellipse 60% 30% at 50% 20%,rgba(200,215,225,.8),transparent 75%),linear-gradient(180deg,#8aa8c0,#6a7a88 55%,#3a3a40)}
.p-sculpt{background:radial-gradient(ellipse 30% 40% at 50% 50%,rgba(200,140,70,.95),transparent 70%),radial-gradient(ellipse 60% 40% at 50% 90%,rgba(230,200,160,.9),transparent 75%),linear-gradient(160deg,#f0dcc0,#c8a070 60%,#8a6030)}
.p-candy{background:radial-gradient(ellipse 35% 35% at 52% 48%,rgba(250,240,240,.85),transparent 65%),radial-gradient(ellipse 55% 55% at 50% 50%,rgba(220,40,50,.9),transparent 75%),linear-gradient(160deg,#e04048,#a01820 60%,#6a0a10)}
.p-rose{background:radial-gradient(circle at 50% 45%,rgba(240,50,50,1) 0,rgba(190,20,30,.95) 22%,transparent 45%),radial-gradient(ellipse 50% 40% at 30% 85%,rgba(60,90,40,.9),transparent 70%),linear-gradient(160deg,#6a1418,#2a0c0c)}
.p-key{background:radial-gradient(ellipse 40% 30% at 45% 45%,rgba(230,235,240,.85),transparent 70%),radial-gradient(ellipse 50% 40% at 70% 80%,rgba(60,110,170,.9),transparent 70%),linear-gradient(160deg,#6a9ac8,#2a5a90 55%,#14304e)}
.p-coins{background:radial-gradient(ellipse 30% 40% at 40% 45%,rgba(240,190,120,.95),transparent 70%),radial-gradient(ellipse 30% 40% at 70% 55%,rgba(200,140,70,.9),transparent 70%),linear-gradient(160deg,#c8965a,#7a4a1c 60%,#3a220a)}
.p-office{background:radial-gradient(ellipse 30% 40% at 50% 35%,rgba(225,190,165,.9),transparent 70%),radial-gradient(ellipse 40% 45% at 50% 85%,rgba(30,30,40,.85),transparent 72%),linear-gradient(160deg,#f4f4f6,#c8c8d0 55%,#8a8a96)}
.p-plant{background:radial-gradient(ellipse 30% 30% at 50% 30%,rgba(140,180,80,.85),transparent 70%),radial-gradient(ellipse 55% 40% at 50% 75%,rgba(200,150,80,.95),transparent 72%),linear-gradient(160deg,#e8d0a0,#a87a40 60%,#5a3e18)}
.p-veg{background:radial-gradient(ellipse 30% 30% at 30% 35%,rgba(230,60,40,.9),transparent 70%),radial-gradient(ellipse 30% 30% at 70% 40%,rgba(240,160,40,.9),transparent 70%),radial-gradient(ellipse 55% 40% at 50% 80%,rgba(70,140,40,.95),transparent 72%),linear-gradient(160deg,#c86a2a,#3a6a20)}
.p-meadow{background:radial-gradient(circle at 50% 40%,rgba(250,250,240,.9) 0,transparent 18%),radial-gradient(ellipse 60% 40% at 50% 85%,rgba(80,140,30,.95),transparent 72%),linear-gradient(180deg,#d8e8a0,#8ab848 50%,#2e5a16)}
.p-yarn{background:radial-gradient(ellipse 35% 30% at 40% 45%,rgba(230,110,150,.9),transparent 70%),radial-gradient(ellipse 35% 30% at 70% 70%,rgba(120,170,90,.85),transparent 70%),linear-gradient(160deg,#c86a8a,#7a3a6a 60%,#3a2040)}
.p-smile{background:radial-gradient(circle at 55% 55%,rgba(250,220,40,1) 0,rgba(240,190,20,.9) 14%,transparent 28%),radial-gradient(ellipse 50% 50% at 30% 30%,rgba(90,190,240,.9),transparent 70%),linear-gradient(160deg,#40a8e0,#1a5aa0 60%,#0e3a70)}
.p-beach{background:radial-gradient(ellipse 30% 45% at 45% 55%,rgba(230,200,180,.9),transparent 70%),radial-gradient(ellipse 60% 30% at 50% 20%,rgba(180,210,230,.9),transparent 75%),linear-gradient(180deg,#a8c4d4,#c8c4b0 55%,#c8a880)}
.p-puppy{background:radial-gradient(ellipse 40% 45% at 50% 50%,rgba(235,215,185,.95),transparent 70%),radial-gradient(ellipse 50% 40% at 50% 90%,rgba(120,90,60,.8),transparent 72%),linear-gradient(160deg,#c8a880,#8a6a48 60%,#4a3624)}
.p-father{background:radial-gradient(ellipse 35% 40% at 40% 40%,rgba(230,200,170,.9),transparent 70%),radial-gradient(ellipse 40% 40% at 70% 70%,rgba(90,70,50,.85),transparent 72%),linear-gradient(160deg,#d8c8a0,#8a7050 60%,#3a2e22)}
.p-gifts{background:radial-gradient(ellipse 30% 30% at 65% 35%,rgba(90,150,220,.9),transparent 70%),radial-gradient(ellipse 35% 30% at 40% 70%,rgba(245,245,250,.95),transparent 70%),linear-gradient(160deg,#eef2f6,#9ab8dc 60%,#4a78b0)}
.p-jewel{background:radial-gradient(ellipse 25% 25% at 40% 45%,rgba(220,190,120,.9),transparent 70%),radial-gradient(ellipse 30% 30% at 65% 60%,rgba(80,130,120,.8),transparent 70%),linear-gradient(160deg,#a89070,#5a4632 60%,#2a2016)}
.p-dress{background:radial-gradient(ellipse 30% 50% at 50% 55%,rgba(245,235,220,.95),transparent 70%),radial-gradient(ellipse 40% 30% at 50% 20%,rgba(120,100,80,.7),transparent 72%),linear-gradient(160deg,#e8dcc8,#b09878 60%,#6a5440)}
.p-hat{background:radial-gradient(ellipse 40% 25% at 50% 25%,rgba(200,170,120,.95),transparent 70%),radial-gradient(ellipse 35% 45% at 50% 65%,rgba(230,205,185,.9),transparent 70%),linear-gradient(160deg,#e0d0b8,#9a7c5c 60%,#5a4430)}
.p-pink{background:radial-gradient(ellipse 35% 35% at 50% 65%,rgba(240,170,190,.95),transparent 70%),radial-gradient(ellipse 30% 30% at 50% 25%,rgba(230,210,200,.9),transparent 70%),linear-gradient(160deg,#f6ecee,#d8b0b8 60%,#a07880)}
.p-hands{background:radial-gradient(ellipse 40% 35% at 45% 50%,rgba(245,245,245,.95),transparent 70%),radial-gradient(ellipse 50% 40% at 50% 90%,rgba(80,80,80,.8),transparent 72%),linear-gradient(160deg,#d8d8d8,#9a9a9a 55%,#4a4a4a)}
.p-forest{background:radial-gradient(ellipse 50% 30% at 50% 25%,rgba(200,225,240,.85),transparent 70%),radial-gradient(ellipse 40% 35% at 30% 60%,rgba(120,170,60,.9),transparent 70%),radial-gradient(ellipse 40% 30% at 70% 80%,rgba(170,60,110,.7),transparent 70%),linear-gradient(180deg,#6fa34a,#3a6a28 60%,#1e3a16)}
.p-falls{background:radial-gradient(ellipse 20% 45% at 55% 50%,rgba(235,240,240,.9),transparent 70%),radial-gradient(ellipse 50% 50% at 20% 40%,rgba(90,150,50,.9),transparent 72%),linear-gradient(160deg,#4f8a3a,#24501e 60%,#102810)}

footer{height:57px;background:var(--footer);color:#aaa;font-size:11px;display:flex;align-items:center;justify-content:center}
</style>
</head>
<body>

<header class="hero" role="img" aria-label="Photo of a lion sitting in golden grass">
  <div class="wrap">
    <div class="brand">StarlitPathway.net<small>by Mara Quinn</small></div>
    <nav class="main-nav">
      <a class="active">Home</a><a>Horoscopes</a><a>Compatibility</a><a>Romance</a><a>About Mara Quinn</a><a>Blog</a>
    </nav>
    <div class="sign-title">Leo</div>
    <div class="sign-sub">Daily Horoscope</div>
    <div class="sign-dates">Jul 23 – Aug 22</div>
    <ul class="zodiac glyphs-list">
      <li><span class="glyph glyphs">&#9800;&#xFE0E;</span>Aries</li>
      <li><span class="glyph glyphs">&#9801;&#xFE0E;</span>Taurus</li>
      <li><span class="glyph glyphs">&#9802;&#xFE0E;</span>Gemini</li>
      <li><span class="glyph glyphs">&#9803;&#xFE0E;</span>Cancer</li>
      <li class="on"><span class="glyph glyphs">&#9804;&#xFE0E;</span>Leo</li>
      <li><span class="glyph glyphs">&#9805;&#xFE0E;</span>Virgo</li>
      <li><span class="glyph glyphs">&#9806;&#xFE0E;</span>Libra</li>
      <li><span class="glyph glyphs">&#9807;&#xFE0E;</span>Scorpio</li>
      <li><span class="glyph glyphs">&#9808;&#xFE0E;</span>Sagittarius</li>
      <li><span class="glyph glyphs">&#9809;&#xFE0E;</span>Capricorn</li>
      <li><span class="glyph glyphs">&#9810;&#xFE0E;</span>Aquarius</li>
      <li><span class="glyph glyphs">&#9811;&#xFE0E;</span>Pisces</li>
    </ul>
  </div>
</header>

<section class="daily">
  <div class="wrap">
    <h1><span class="leo-mark glyphs">&#9804;&#xFE0E;</span>Leo Daily Horoscope</h1>
    <div class="date">February 16th, 2015</div>
    <div class="tabs"><span>Yesterday</span><span class="active">Today</span><span>Tomorrow</span></div>
    <p class="text">Today brings a warm spark to your plans, Leo. Trust the quiet voice that tells you to slow down and listen. A friend may offer a fresh idea worth exploring, and your generous heart will find the right moment to share it with those you love most.</p>
    <div class="meta"><span><b>INTENSITY</b>67%</span><span><b>KEYWORDS</b>Unconcealed, Mosaic</span><span><b>MOOD</b>Touchy</span></div>
    <span class="btn">Find Out More About Today's Planets</span>
    <div class="photo ph" role="img" aria-label="Photo of a lion resting in the savanna"></div>
    <div class="rating">RATING <i></i><i></i><i></i><i class="off"></i><i class="off"></i></div>
  </div>
</section>

<section class="periods">
  <div class="wrap">
    <div class="cards">
      <div class="card">
        <div class="photo ph p-hands" role="img" aria-label="Photo of open hands holding sand"><span>Weekly<br>Horoscope</span></div>
        <p>See what the stars hold for you this week and plan each day with calm confidence.</p>
        <span class="more">Read More</span>
      </div>
      <div class="card sel">
        <div class="photo ph p-forest" role="img" aria-label="Photo of a green valley with flowers"><span>Monthly<br>Horoscope</span></div>
        <p>See what the stars hold for you this month and plan each week with calm confidence.</p>
        <span class="more">Read More</span>
      </div>
      <div class="card">
        <div class="photo ph p-falls" role="img" aria-label="Photo of a waterfall among green trees"><span>Yearly<br>Horoscope</span></div>
        <p>See what the stars hold for you this year and plan each season with calm confidence.</p>
        <span class="more">Read More</span>
      </div>
    </div>
  </div>
</section>

<section class="compat">
  <div class="wrap">
    <h2 class="sec-title">Leo Compatibility</h2>
    <div class="overview ph" role="img" aria-label="Photo of two red hearts on a wooden table"><span class="overlay-label">Overview</span></div>
    <div class="topics">
      <div class="topic ph t-dating" role="img" aria-label="Photo of a couple embracing"><span class="overlay-label">Dating</span></div>
      <div class="topic ph t-marriage" role="img" aria-label="Photo of a bride and groom outdoors"><span class="overlay-label">Marriage</span></div>
      <div class="topic ph t-passion" role="img" aria-label="Dark photo with red glowing light"><span class="overlay-label">Passion</span></div>
      <div class="topic ph t-financial" role="img" aria-label="Photo of stacked coins"><span class="overlay-label">Financial</span></div>
    </div>
  </div>
</section>

<section class="app" role="img" aria-label="Starry night sky background">
  <div class="wrap">
    <h2>Get Today's <b>Horoscope</b><br>on your <b>smartphone</b></h2>
    <span class="btn">DOWNLOAD</span>
    <div class="phones">
      <div class="phone"><div role="img" aria-label="App screen with a portrait photo"></div></div>
      <div class="phone"><div role="img" aria-label="App screen with a portrait photo"></div></div>
    </div>
  </div>
</section>

<section class="bar"><span class="leo-mark glyphs">&#9804;&#xFE0E;</span>Leo Compatibility</section>

<section class="row-sec" style="height:440px">
  <div class="wrap">
    <h2 class="sec-title">About</h2>
    <svg class="arrow l" viewBox="0 0 18 30"><path d="M15 3 4 15l11 12" fill="none" stroke="#ccc" stroke-width="3"/></svg>
    <svg class="arrow r" viewBox="0 0 18 30"><path d="M3 3l11 12L3 27" fill="none" stroke="#ccc" stroke-width="3"/></svg>
    <div class="tiles">
      <div class="tile"><div class="photo ph p-lion" role="img" aria-label="Photo of a lion"></div><p>About Leo</p></div>
      <div class="tile sel"><div class="photo ph p-fire" role="img" aria-label="Photo of flames"></div><p>Leo is a Fire Sign</p></div>
      <div class="tile"><div class="photo ph p-sky" role="img" aria-label="Photo of clouds with a motivational slogan"></div><p>Leo is a Fixed Sign</p></div>
      <div class="tile"><div class="photo ph p-planet" role="img" aria-label="Photo of the sun rising over a planet"></div><p>Leo, Your Ruling Planet is the Sun</p></div>
    </div>
  </div>
</section>

<section class="row-sec grey" style="height:455px">
  <div class="wrap">
    <h2 class="sec-title">Love And Romance</h2>
    <svg class="arrow l" viewBox="0 0 18 30"><path d="M15 3 4 15l11 12" fill="none" stroke="#ccc" stroke-width="3"/></svg>
    <svg class="arrow r" viewBox="0 0 18 30"><path d="M3 3l11 12L3 27" fill="none" stroke="#ccc" stroke-width="3"/></svg>
    <div class="tiles">
      <div class="tile"><div class="photo ph p-couple" role="img" aria-label="Photo of a couple sitting by the sea"></div><p>Could You Be Soul Mates? Consult the Elements of the Zodiac!</p></div>
      <div class="tile"><div class="photo ph p-sculpt" role="img" aria-label="Photo of a heart-shaped sculpture"></div><p>Eight Things Everyone Should Know about Love</p></div>
      <div class="tile"><div class="photo ph p-candy" role="img" aria-label="Photo of a red candy with a message"></div><p>How Committed Is He? Long-Term Love Signals</p></div>
      <div class="tile"><div class="photo ph p-rose" role="img" aria-label="Photo of a red rose"></div><p>How To Be Your Best Romantic Self, Leo</p></div>
    </div>
  </div>
</section>

<section class="row-sec" style="height:480px">
  <div class="wrap">
    <h2 class="sec-title" style="top:62px">Career And Money</h2>
    <svg class="arrow l" viewBox="0 0 18 30" style="top:232px"><path d="M15 3 4 15l11 12" fill="none" stroke="#ccc" stroke-width="3"/></svg>
    <svg class="arrow r" viewBox="0 0 18 30" style="top:232px"><path d="M3 3l11 12L3 27" fill="none" stroke="#ccc" stroke-width="3"/></svg>
    <div class="tiles" style="top:130px">
      <div class="tile"><div class="photo ph p-key" role="img" aria-label="Photo of a key on a printed page"></div><p>Are You a Leader or a Follower, Leo?</p></div>
      <div class="tile"><div class="photo ph p-coins" role="img" aria-label="Photo of stacked coins"></div><p>Are You a Spender or Saver, Leo?</p></div>
      <div class="tile"><div class="photo ph p-office" role="img" aria-label="Photo of a businesswoman in an office"></div><p>Are You on the Right Career Path? Make Your Best Prediction</p></div>
      <div class="tile"><div class="photo ph p-plant" role="img" aria-label="Photo of coins with a growing plant"></div><p>Astrology and Finances: Leo Money Profile</p></div>
    </div>
  </div>
</section>

<section class="row-sec grey" style="height:468px">
  <div class="wrap">
    <h2 class="sec-title" style="top:52px">Well Being</h2>
    <svg class="arrow l" viewBox="0 0 18 30" style="top:220px"><path d="M15 3 4 15l11 12" fill="none" stroke="#ccc" stroke-width="3"/></svg>
    <svg class="arrow r" viewBox="0 0 18 30" style="top:220px"><path d="M3 3l11 12L3 27" fill="none" stroke="#ccc" stroke-width="3"/></svg>
    <div class="tiles" style="top:116px">
      <div class="tile"><div class="photo ph p-veg" role="img" aria-label="Photo of fresh vegetables and fruit"></div><p>A Diet and Fitness Guide for Leo</p></div>
      <div class="tile"><div class="photo ph p-meadow" role="img" aria-label="Photo of a dandelion in green grass"></div><p>A Spring Cleaning Guide for Leo</p></div>
      <div class="tile"><div class="photo ph p-yarn" role="img" aria-label="Photo of knitting yarn and needles"></div><p>Astrology and Hobbies: Find a New Pastime, Leo</p></div>
      <div class="tile"><div class="photo ph p-smile" role="img" aria-label="Photo of colourful balls"></div><p>Don't Worry, Be Happy, Leo!</p></div>
    </div>
  </div>
</section>

<section class="row-sec" style="height:466px">
  <div class="wrap">
    <h2 class="sec-title" style="top:52px">Friends And Family</h2>
    <svg class="arrow l" viewBox="0 0 18 30" style="top:220px"><path d="M15 3 4 15l11 12" fill="none" stroke="#ccc" stroke-width="3"/></svg>
    <svg class="arrow r" viewBox="0 0 18 30" style="top:220px"><path d="M3 3l11 12L3 27" fill="none" stroke="#ccc" stroke-width="3"/></svg>
    <div class="tiles" style="top:116px">
      <div class="tile"><div class="photo ph p-beach" role="img" aria-label="Photo of an expectant mother on a beach"></div><p>A Guide to Getting Pregnant and Parenting for Leo</p></div>
      <div class="tile"><div class="photo ph p-puppy" role="img" aria-label="Photo of a fluffy puppy"></div><p>Best Pets for Leo</p></div>
      <div class="tile"><div class="photo ph p-father" role="img" aria-label="Photo of a father and child"></div><p>Father's Day Gift Guide for Leo</p></div>
      <div class="tile"><div class="photo ph p-gifts" role="img" aria-label="Photo of wrapped gift boxes"></div><p>Great Gift Ideas for Leo</p></div>
    </div>
  </div>
</section>

<section class="row-sec grey" style="height:449px">
  <div class="wrap">
    <h2 class="sec-title" style="top:44px">Fashion And Beauty</h2>
    <svg class="arrow l" viewBox="0 0 18 30" style="top:208px"><path d="M15 3 4 15l11 12" fill="none" stroke="#ccc" stroke-width="3"/></svg>
    <svg class="arrow r" viewBox="0 0 18 30" style="top:208px"><path d="M3 3l11 12L3 27" fill="none" stroke="#ccc" stroke-width="3"/></svg>
    <div class="tiles" style="top:104px">
      <div class="tile"><div class="photo ph p-jewel" role="img" aria-label="Photo of jewellery and accessories"></div><p>Beauty Guide for Leo</p></div>
      <div class="tile"><div class="photo ph p-dress" role="img" aria-label="Photo of a woman in a summer dress"></div><p>Fashion For Leo: An Astrological Guide to Style</p></div>
      <div class="tile"><div class="photo ph p-hat" role="img" aria-label="Photo of a woman wearing a hat"></div><p>Style Guide: A Fashion Makeover for Leo</p></div>
      <div class="tile"><div class="photo ph p-pink" role="img" aria-label="Photo of a woman in a pink skirt"></div><p>Beauty Guide for Leo</p></div>
    </div>
  </div>
</section>

<footer>Copyright 2015 StarlitPathway.net. All Rights Reserved.</footer>

</body>
</html>
```